business card for LWR pty ltd

We require a business card that stands out . I have included our company flyer and would like the services listed to be put on the card so when we Give out the cards to customers they have an idea of services we provide. need the winning design to be in editable photo shop format, editable iMac pages format or editable windows publisher format, so that I can enter in names, email addresses, phone numbers etc myself. I have included a pdf documents of info / items needed on the card to use as reference please.
Updates

need more submissions

Need extra days to review

Sick

Target Market(s)

new customers

Contact Information for Business Card

details are on attached business card requirements file

Requirements
Must have
• I have attached a list of must haves

```html
<!DOCTYPE html>
<html lang="en">
<head>
<meta charset="utf-8">
<title>LWR pty ltd – Business Card</title>
<link href="https://fonts.googleapis.com/css2?family=Montserrat:wght@400;500;700&family=Titan+One&display=swap" rel="stylesheet">
<style>
  :root {
    --blue: #1737d8;
    --teal: #169b9b;
    --green: #3ccf2a;
    --panel: #1c1d1f;
    --ink: #141414;
    --icon: #2aaed0;
    --white: #ffffff;
    --silver: #c9cdd1;
  }
  * { margin: 0; padding: 0; box-sizing: border-box; }
  html, body { width: 1200px; height: 686px; overflow: hidden; background: var(--white); }
  .card {
    position: relative; width: 1200px; height: 686px; overflow: hidden;
    background: var(--white); font-family: "Montserrat", Arial, sans-serif; color: var(--ink);
  }
  .company-name {
    position: absolute; left: 40px; top: 84px;
    font-family: "Titan One", "Arial Black", sans-serif; font-size: 46px; letter-spacing: 1px;
  }
  .company-name .w1 { color: var(--blue); }
  .company-name .w2 { color: var(--teal); }
  .company-name .w3 { color: var(--green); }
  .hero-photo {
    position: absolute; left: 389px; top: 0; width: 811px; height: 341px;
    background: linear-gradient(180deg, #0b0b0c 0%, #1d1e20 38%, #3a2c22 52%, #8d4a24 68%, #b8622e 85%, #a7582b 100%);
  }
  .hero-mark {
    position: absolute; left: 640px; top: 36px;
    font-family: "Montserrat", Arial, sans-serif; font-weight: 700; font-size: 92px;
    color: var(--silver); letter-spacing: 6px;
  }
  .hero-rule {
    position: absolute; left: 451px; top: 341px; width: 412px; height: 10px;
    background: linear-gradient(90deg, var(--blue), var(--green));
  }
  .name-panel { position: absolute; left: 0; top: 242px; }
  .person-name {
    position: absolute; left: 40px; top: 276px; color: var(--white);
    font-size: 42px; letter-spacing: 0.5px;
  }
  .person-name b { font-weight: 700; }
  .person-name span { font-weight: 400; }
  .person-role {
    position: absolute; left: 40px; top: 326px; color: var(--white);
    font-size: 24px; font-weight: 500;
  }
  .fleet-photo {
    position: absolute; left: 200px; top: 418px; width: 440px; height: 250px;
    background: radial-gradient(ellipse at 55% 55%, rgba(150,150,150,0.28), rgba(200,200,200,0.12) 60%, rgba(255,255,255,0) 80%);
  }
  .contact { position: absolute; left: 22px; list-style: none; }
  .contact li { position: absolute; left: 0; display: flex; align-items: flex-start; width: 520px; }
  .contact svg { width: 30px; height: 30px; flex: none; margin-right: 14px; }
  .contact p { font-size: 22px; font-weight: 500; line-height: 30px; }
  .bottom-bar {
    position: absolute; left: 0; top: 663px; width: 520px; height: 21px;
    background: linear-gradient(90deg, var(--blue), var(--green));
  }
  .services-title {
    position: absolute; left: 464px; top: 358px; text-align: center; width: 170px;
    font-family: "Titan One", "Arial Black", sans-serif; font-size: 34px; line-height: 40px;
    background: linear-gradient(90deg, var(--blue), var(--teal) 55%, var(--green));
    -webkit-background-clip: text; background-clip: text; color: transparent;
  }
  .services { position: absolute; left: 664px; top: 358px; list-style: none; }
  .services li {
    position: relative; padding-left: 45px; font-size: 23px; font-weight: 500; line-height: 28.6px;
  }
  .services li::before {
    content: ""; position: absolute; left: 4px; top: 8px; width: 12px; height: 12px;
    background: var(--ink); transform: rotate(45deg);
  }
</style>
</head>
<body>
<div class="card">
  <h1 class="company-name"><span class="w1">LWR</span> <span class="w2">PTY</span> <span class="w3">LTD</span></h1>

  <div class="hero-photo" role="img" aria-label="Photo of a road train hauling three side-tipper trailers on red outback dirt under a dark metal mesh backdrop"></div>
  <div class="hero-mark">LWR</div>
  <div class="hero-rule"></div>

  <div class="fleet-photo" role="img" aria-label="Faint photo of parked road train prime movers"></div>

  <svg class="name-panel" width="490" height="170" viewBox="0 0 490 170" aria-hidden="true">
    <path d="M0 0 H484 L420 150 Q412 169 392 169 H0 Z" fill="#1c1d1f"/>
  </svg>
  <div class="person-name"><b>DANIEL</b> <span>VARGA</span></div>
  <div class="person-role">Director</div>

  <ul class="contact">
    <li style="top:448px">
      <svg viewBox="0 0 24 24"><path d="M6.6 10.8a15.1 15.1 0 0 0 6.6 6.6l2.2-2.2a1 1 0 0 1 1-.25 11.4 11.4 0 0 0 3.6.57 1 1 0 0 1 1 1V20a1 1 0 0 1-1 1A17 17 0 0 1 3 4a1 1 0 0 1 1-1h3.5a1 1 0 0 1 1 1c0 1.25.2 2.45.57 3.57a1 1 0 0 1-.25 1z" fill="none" stroke="#2aaed0" stroke-width="1.8"/></svg>
      <p>123 4567 890</p>
    </li>
    <li style="top:505px">
      <svg viewBox="0 0 24 24"><circle cx="12" cy="12" r="10" fill="#2aaed0"/><path d="M7 6c2 1 1 3 3 3s1 3-1 4-1 4-2 4M15 5c-1 2 1 3 2 4s3 0 3 2M14 20c0-2 2-2 2-4s2-2 3-2" fill="none" stroke="#fff" stroke-width="1.4"/></svg>
      <p>email@lwrhaulage.com.au<br>www.websiteaddress.com</p>
    </li>
    <li style="top:592px">
      <svg viewBox="0 0 24 24"><path d="M12 3 2 12h3v9h5v-6h4v6h5v-9h3z" fill="#2aaed0"/></svg>
      <p>123, main street, your city,New York<br>USA 456123</p>
    </li>
  </ul>

  <div class="bottom-bar"></div>

  <h2 class="services-title">OUR<br>SERVICES</h2>
  <ul class="services">
    <li>Over size loads/ Hot shot loads</li>
    <li>Heavy Vehicle Recovery Services</li>
    <li>Road building /Maintenance</li>
    <li>Earth Works</li>
    <li>Sand Metal Supply &amp; Cartage</li>
    <li>Mine Site Accredited</li>
    <li>Road Train Tankers</li>
    <li>Road Train Flate Stop</li>
    <li>Drop Deck Trailers</li>
    <li>Equipment &amp; Operators</li>
    <li>Road Train Tappers</li>
  </ul>
</div>
</body>
</html>
```